Antigen Preservation Center

The company will provide a contract research services to stabilize various viruses, viral vectors, and vaccines. It may offer some licensing opportunities for stabilizing technologies. Main area of applications are pharmaceutical, therapeutic, and vaccination field. The company aspires to develop room temperature vaccines for global distribution beyond the current cold chain.
Updates

Target Market(s)

pharmaceutical, therapeutic and vaccination fields

Coding

Number of Pages Required

4 page

Requirements
Must have
• Incorporate a APC logo, attached at the bottom, on the Web page

```html
<!DOCTYPE html>
<html lang="en">
<head>
<meta charset="utf-8">
<title>Antigen Preservation Center</title>
<link rel="stylesheet" href="https://fonts.googleapis.com/css2?family=Montserrat:wght@400;500;600;700&family=Open+Sans:wght@400;600&display=swap">
<style>
:root{
  --green:#4cc96f;
  --green-dark:#36b45a;
  --gold:#c9a227;
  --ink:#2b2b2b;
  --muted:#8a8a8a;
  --dark:#1f1f1f;
  --slate:#6b8580;
  --white:#ffffff;
  --line:#e4e4e4;
}
*{margin:0;padding:0;box-sizing:border-box}
html,body{width:1200px;height:3742px;overflow:hidden}
body{font-family:'Open Sans',sans-serif;color:var(--ink);background:var(--white);position:relative}
.abs{position:absolute}
section,header,footer{position:absolute;left:0;width:1200px}
.h-title{font-family:'Montserrat',sans-serif;font-weight:700;font-size:28px;text-align:center;letter-spacing:1px;position:absolute;left:0;width:1200px}
.h-title .hl{color:var(--green)}
.divider{position:absolute;left:575px;width:50px;height:14px}
.btn{position:absolute;font-family:'Montserrat',sans-serif;font-weight:700;font-size:12px;letter-spacing:1px;color:var(--white);background:var(--gold);border-radius:4px;text-align:center;box-shadow:0 3px 6px rgba(0,0,0,.2)}
.brand{position:absolute;display:flex;align-items:center;gap:12px;font-family:'Montserrat',sans-serif;font-weight:700;line-height:1.1}
.brand .dot{width:40px;height:40px;border-radius:50%;background:var(--green)}
.lorem{font-size:12px;color:var(--muted);line-height:1.55}

/* header */
.site-header{top:0;height:100px;background:var(--white)}
.site-header .brand{left:112px;top:24px;font-size:15px;color:var(--green)}
.topbar{position:absolute;right:112px;top:18px;display:flex;gap:22px;align-items:center;font-size:12px;color:#555}
.topbar .req{background:var(--green);color:#fff;font-family:'Montserrat',sans-serif;font-weight:700;font-size:11px;padding:7px 18px;border-radius:14px}
.nav{position:absolute;right:112px;top:62px;display:flex;gap:50px;font-family:'Montserrat',sans-serif;font-size:12px;color:#777}
.nav .on{color:var(--green);font-weight:700}

/* hero */
.hero{top:100px;height:499px;background:radial-gradient(ellipse at 68% 45%,#8fa0aa 0%,#3c474e 38%,#0d0f11 75%)}
.hero-photo{position:absolute;left:420px;top:0;width:780px;height:499px;background:radial-gradient(ellipse at 55% 50%,rgba(230,235,238,.55) 0%,rgba(120,135,145,.2) 40%,rgba(0,0,0,0) 70%)}
.hero h1{position:absolute;left:110px;top:128px;font-family:'Montserrat',sans-serif;font-size:46px;line-height:1.06;font-weight:700;color:var(--green);letter-spacing:1px}
.hero h1 span{color:var(--white)}
.hero p{position:absolute;left:110px;top:270px;width:430px;font-size:11px;color:#ddd;line-height:1.5;text-transform:uppercase}
.hero .btn{left:110px;top:325px;width:134px;height:40px;line-height:40px}
.dots{position:absolute;left:568px;top:465px;display:flex;gap:6px}
.dots i{width:9px;height:9px;border-radius:50%;border:1px solid #fff;display:block}
.dots i.on{background:var(--gold);border-color:var(--gold)}

/* welcome */
.welcome{top:599px;height:454px}
.welcome .pre{position:absolute;left:0;width:1200px;top:58px;text-align:center;font-family:'Montserrat',sans-serif;font-weight:700;font-size:20px;letter-spacing:1px}
.video{position:absolute;left:210px;top:162px;width:360px;height:237px;border:3px solid #3b78c8;background:linear-gradient(135deg,#b9d8f0,#3f7fc4 55%,#c94a5c);}
.play{position:absolute;left:155px;top:93px;width:50px;height:50px;border-radius:50%;background:var(--green);border:3px solid #fff}
.intro{position:absolute;left:620px;top:158px;width:380px;font-family:'Montserrat',sans-serif;font-weight:700;font-size:13px;line-height:1.6;letter-spacing:.5px;color:#333;text-transform:uppercase}
.feature{position:absolute;left:620px;width:400px;display:flex;gap:16px}
.feature .ic{flex:none;width:64px;height:64px;border-radius:50%;border:2px solid #ddd}
.feature h4{font-family:'Montserrat',sans-serif;font-size:14px;color:var(--green);margin:6px 0 4px}

/* services */
.services{top:1053px;height:509px;background:linear-gradient(135deg,#5ad27c,#3dbd62)}
.services .h-title{top:44px;color:#fff}
.arrow{position:absolute;width:18px;height:28px}
.card{position:absolute;top:142px;width:239px;height:310px;background:#fff;border-radius:3px;box-shadow:0 4px 10px rgba(0,0,0,.15);text-align:center}
.card .photo{height:150px;border-radius:3px 3px 0 0}
.card h3{font-family:'Montserrat',sans-serif;font-size:12.5px;font-weight:700;color:var(--gold);margin:22px 20px 8px;line-height:1.35}
.card .lorem{margin:0 22px}
.card .more{position:absolute;left:50%;transform:translateX(-50%);bottom:24px;width:94px;height:26px;line-height:26px;border-radius:4px;font-family:'Montserrat',sans-serif;font-size:9px;font-weight:700;color:#fff;background:var(--gold)}
.card.raised{top:135px;height:330px;box-shadow:0 10px 24px rgba(0,0,0,.3)}
.card.raised .more{background:var(--green)}
.card.grey .more{background:#6f6f6f}
.card.grey h3{color:#333}

/* who we serve */
.serve{top:1562px;height:379px}
.serve .h-title{top:48px;color:var(--green)}
.serve-item{position:absolute;top:130px;width:220px;text-align:center}
.serve-item .ring{width:92px;height:92px;border-radius:50%;border:3px solid var(--gold);margin:0 auto}
.serve-item h4{font-family:'Montserrat',sans-serif;font-size:15px;font-weight:700;margin-top:22px;color:var(--gold)}
.serve .btn{left:523px;top:290px;width:154px;height:34px;line-height:34px;font-size:11px}

/* reviews */
.reviews{top:1941px;height:275px;background:radial-gradient(ellipse at 50% 40%,#869d98,#5d7772)}
.reviews .h-title{top:44px;color:#fff}
.review{position:absolute;top:128px;width:420px;display:flex;gap:26px}
.review .avatar{flex:none;width:86px;height:86px;border-radius:50%;background:linear-gradient(#d9d2c8,#8c857c);border:3px solid #fff}
.review p{font-size:11.5px;color:#eef;line-height:1.55;font-style:italic}
.review .who{margin-top:12px;font-family:'Montserrat',sans-serif;font-weight:700;font-size:12px;color:#fff}
.review .who b{color:var(--gold);font-size:11px;margin-left:10px;letter-spacing:2px}
.vsep{position:absolute;left:599px;top:125px;width:1px;height:95px;background:rgba(255,255,255,.4)}

/* why choose */
.why{top:2216px;height:486px}
.why .h-title{top:44px;color:var(--green)}
.hub{position:absolute;left:487px;top:167px;width:224px;height:224px;border-radius:50%;border:10px solid #f1f1f1;background:#fff;box-shadow:0 0 0 1px #e7e7e7}
.hub .brand{left:0;width:204px;top:70px;flex-direction:column;gap:8px;text-align:center;color:var(--green);font-size:15px}
.hub .brand .dot{width:46px;height:46px}
.reason{position:absolute;width:340px;display:flex;gap:14px;align-items:flex-start}
.reason .ic{flex:none;width:44px;height:44px;border-radius:50%;background:var(--gold)}
.reason h4{font-family:'Montserrat',sans-serif;font-size:12px;font-weight:700;margin:2px 0 4px;color:#444}
.reason.left{left:78px;flex-direction:row-reverse;text-align:right}
.reason.right{left:752px}
.reason .ic.g{background:#8e8e8e}
.why .btn{left:538px;top:414px;width:122px;height:34px;line-height:34px;font-size:11px}

/* news */
.news{top:2702px;height:499px;background:linear-gradient(135deg,#d0a935,#bf961c)}
.news .h-title{top:54px;color:#fff}
.post{position:absolute;top:137px;width:235px;height:310px;background:#fff;border-radius:3px;box-shadow:0 4px 10px rgba(0,0,0,.2);text-align:center}
.post .photo{height:168px;border-radius:3px 3px 0 0}
.post .date{font-size:9px;color:#777;margin-top:14px}
.post h3{font-family:'Montserrat',sans-serif;font-size:11.5px;font-weight:700;margin:6px 20px;line-height:1.35}
.post .lorem{margin:0 20px;font-size:10px}
.post .plus{position:absolute;right:0;bottom:0;width:26px;height:26px;background:#6f6f6f;color:#fff;font-size:16px;line-height:26px}
.post.raised h3{color:var(--green)}
.post.raised .plus{background:var(--green)}
.post.raised .lorem{color:#555}

/* accreditations */
.accred{top:3201px;height:250px}
.accred .h-title{top:50px}
.partner{position:absolute;top:148px;width:150px;display:flex;align-items:center;justify-content:center;gap:8px;font-family:'Montserrat',sans-serif;font-weight:600;font-size:19px;color:#555}
.partner i{width:18px;height:18px;border-radius:50%;background:#777;display:block}

/* footer */
.site-footer{top:3451px;height:291px;background:var(--dark);color:#bbb}
.site-footer .brand{left:112px;top:80px;color:#fff;font-size:15px}
.site-footer .brand .dot{background:#fff}
.social{position:absolute;left:158px;top:152px;display:flex;gap:6px}
.social i{width:20px;height:20px;border-radius:50%;border:1px solid #ccc;display:block}
.fcol{position:absolute;top:60px}
.fcol h4{font-family:'Montserrat',sans-serif;font-size:14px;color:#fff;font-weight:700;margin-bottom:14px}
.fcol h4 span{color:var(--green)}
.fcol ul{list-style:none;font-size:11px;line-height:22px}
.fcol li:before{content:"› ";color:var(--green)}
.contact-row{display:flex;gap:10px;font-size:11px;line-height:1.5;margin-bottom:10px;color:#ccc}
.contact-row i{flex:none;width:10px;height:10px;border-radius:50%;background:var(--green);margin-top:3px}
.field{width:210px;height:30px;border-radius:15px;background:#fff;margin-bottom:8px;font-size:10px;color:#999;padding:8px 14px}
.subscribe{width:120px;height:32px;line-height:32px;border-radius:16px;background:var(--green);color:#fff;text-align:center;font-family:'Montserrat',sans-serif;font-weight:700;font-size:11px}
.bottombar{position:absolute;left:112px;right:112px;top:255px;display:flex;justify-content:space-between;font-size:10px;color:#999;letter-spacing:.5px}
</style>
</head>
<body>

<header class="site-header">
  <div class="brand"><span class="dot"></span><span>ANTIGEN<br>PRESERVATION<br><span style="color:#444">CENTER</span></span></div>
  <div class="topbar">
    <span>&#9742; +1 555 010 1234</span>
    <span>&#9993; info@antigenpreservation.example</span>
    <span class="req">REQUEST A SERVICE</span>
  </div>
  <nav class="nav"><span class="on">HOME</span><span>ABOUT US</span><span>SERVICES</span><span>WHO WE SERVE</span><span>NEWS</span><span>CONTACT US</span></nav>
</header>

<section class="hero">
  <div class="hero-photo" role="img" aria-label="Vaccine vials resting in a white foam shipping case with cold mist"></div>
  <h1>ANTIGEN<br>PRESERVATION<br><span>CENTER</span></h1>
  <p>The company aspires to develop room temperature vaccines for global distribution beyond the current cold chain.</p>
  <div class="btn">CONTACT US</div>
  <div class="dots"><i></i><i></i><i class="on"></i><i></i></div>
</section>

<section class="welcome">
  <div class="pre">WELCOME TO</div>
  <div class="h-title" style="top:86px"><span class="hl">ANTIGEN PRESERVATION</span> CENTER</div>
  <svg class="divider" style="top:128px" viewBox="0 0 50 14"><line x1="0" y1="7" x2="18" y2="7" stroke="#ccc"/><line x1="32" y1="7" x2="50" y2="7" stroke="#ccc"/><circle cx="25" cy="7" r="4" fill="#4cc96f"/></svg>
  <div class="video" role="img" aria-label="Laboratory pipette filling colourful test tubes, video still"><span class="play"></span></div>
  <div class="intro">We provide a contract research services to stabilize various viruses, viral vectors, and vaccines.</div>
  <div class="feature" style="top:236px"><span class="ic"></span><div><h4>OUR GOAL</h4><p class="lorem">OUR GOAL is a simple statement of our aims, kept short and clear for readers here.</p></div></div>
  <div class="feature" style="top:326px"><span class="ic"></span><div><h4>OUR APPROACH</h4><p class="lorem">OUR APPROACH is a short note on how we work, step by step with every partner.</p></div></div>
</section>

<section class="services">
  <div class="h-title">SERVICES WE PROVIDE</div>
  <svg class="divider" style="top:86px" viewBox="0 0 50 14"><line x1="0" y1="7" x2="18" y2="7" stroke="#fff"/><line x1="32" y1="7" x2="50" y2="7" stroke="#fff"/><circle cx="25" cy="7" r="4" fill="#fff"/></svg>
  <svg class="arrow" style="left:138px;top:284px" viewBox="0 0 18 28"><polyline points="14,2 4,14 14,26" fill="none" stroke="#fff" stroke-width="3"/></svg>
  <svg class="arrow" style="left:1044px;top:284px" viewBox="0 0 18 28"><polyline points="4,2 14,14 4,26" fill="none" stroke="#fff" stroke-width="3"/></svg>
  <div class="card" style="left:210px"><div class="photo" role="img" aria-label="Gloved hand holding a test tube under blue light" style="background:linear-gradient(135deg,#1d2f5a,#5a79b8)"></div><h3>PHYSICAL STABILITY</h3><p class="lorem">Short text on this service goes here, kept to a few plain lines for now.</p><div class="more">READ MORE</div></div>
  <div class="card raised" style="left:482px"><div class="photo" role="img" aria-label="Glass flasks and lab equipment on a bench" style="background:linear-gradient(135deg,#6d6d6d,#d9d9d9)"></div><h3>PREFORMULATION AND<br>FORMULATION STUDIES</h3><p class="lorem">Short text on this service goes here, kept to a few plain lines for now.</p><div class="more">READ MORE</div></div>
  <div class="card grey" style="left:751px"><div class="photo" role="img" aria-label="Scientist working with sample plates in a bright lab" style="background:linear-gradient(135deg,#8fc3e6,#f0f6fa)"></div><h3>CHEMICAL STABILITY</h3><p class="lorem">Short text on this service goes here, kept to a few plain lines for now.</p><div class="more">READ MORE</div></div>
</section>

<section class="serve">
  <div class="h-title">WHO WE SERVE</div>
  <svg class="divider" style="top:90px" viewBox="0 0 50 14"><line x1="0" y1="7" x2="18" y2="7" stroke="#ccc"/><line x1="32" y1="7" x2="50" y2="7" stroke="#ccc"/><circle cx="25" cy="7" r="4" fill="#c9a227"/></svg>
  <div class="serve-item" style="left:219px"><div class="ring"></div><h4>PHARMACEUTICAL</h4></div>
  <div class="serve-item" style="left:489px"><div class="ring" style="border-color:var(--green)"></div><h4 style="color:var(--green)">THERAPEUTIC</h4></div>
  <div class="serve-item" style="left:761px"><div class="ring" style="border-color:#777"></div><h4 style="color:#444">VACCINATION FIELD</h4></div>
  <div class="btn">REQUEST A SERVICE</div>
</section>

<section class="reviews">
  <div class="h-title">CLIENT REVIEWS</div>
  <svg class="divider" style="top:86px" viewBox="0 0 50 14"><line x1="0" y1="7" x2="18" y2="7" stroke="#fff"/><line x1="32" y1="7" x2="50" y2="7" stroke="#fff"/><circle cx="25" cy="7" r="4" fill="#fff"/></svg>
  <svg class="arrow" style="left:138px;top:148px" viewBox="0 0 18 28"><polyline points="14,2 4,14 14,26" fill="none" stroke="#fff" stroke-width="3"/></svg>
  <svg class="arrow" style="left:1044px;top:148px" viewBox="0 0 18 28"><polyline points="4,2 14,14 4,26" fill="none" stroke="#fff" stroke-width="3"/></svg>
  <div class="review" style="left:210px"><span class="avatar" role="img" aria-label="Client portrait"></span><div><p>"A short client note of thanks sits here, two or three lines long, about the fine work done and the care shown."</p><div class="who">Nora Lind <b>★★★★★</b></div></div></div>
  <div class="vsep"></div>
  <div class="review" style="left:638px"><span class="avatar" role="img" aria-label="Client portrait"></span><div><p>"A short client note of thanks sits here, two or three lines long, about the fine work done and the care shown."</p><div class="who">Owen Hale <b>★★★★★</b></div></div></div>
</section>

<section class="why">
  <div class="h-title">WHY CHOOSE US</div>
  <svg class="divider" style="top:86px" viewBox="0 0 50 14"><line x1="0" y1="7" x2="18" y2="7" stroke="#ccc"/><line x1="32" y1="7" x2="50" y2="7" stroke="#ccc"/><circle cx="25" cy="7" r="4" fill="#4cc96f"/></svg>
  <div class="hub"><div class="brand"><span class="dot"></span><span>ANTIGEN<br>PRESERVATION<br><span style="color:#444;font-size:12px;letter-spacing:2px">CENTER</span></span></div></div>
  <div class="reason left" style="top:124px"><span class="ic"></span><div><h4>YEARS OF EXPERIENCE</h4><p class="lorem">Short line of text on this point here,<br>kept brief and easy to read.</p></div></div>
  <div class="reason left" style="top:218px"><span class="ic g"></span><div><h4>24/7 SUPPORT SERVICES</h4><p class="lorem">Short line of text on this point here,<br>kept brief and easy to read.</p></div></div>
  <div class="reason left" style="top:310px"><span class="ic" style="background:var(--green)"></span><div><h4>BEST QUALIFIED TEAM</h4><p class="lorem">Short line of text on this point here,<br>kept brief and easy to read.</p></div></div>
  <div class="reason right" style="top:124px"><span class="ic" style="background:var(--green)"></span><div><h4>SPEED OF RESPONSE</h4><p class="lorem">Short line of text on this point here,<br>kept brief and easy to read.</p></div></div>
  <div class="reason right" style="top:218px"><span class="ic g"></span><div><h4>GLOBAL DISTRIBUTION</h4><p class="lorem">Short line of text on this point here,<br>kept brief and easy to read.</p></div></div>
  <div class="reason right" style="top:310px"><span class="ic"></span><div><h4>TEMPERATURE STABILIZATION</h4><p class="lorem">Short line of text on this point here,<br>kept brief and easy to read.</p></div></div>
  <div class="btn">CONTACT US</div>
</section>

<section class="news">
  <div class="h-title">OUR NEWS</div>
  <svg class="divider" style="top:96px" viewBox="0 0 50 14"><line x1="0" y1="7" x2="18" y2="7" stroke="#fff"/><line x1="32" y1="7" x2="50" y2="7" stroke="#fff"/><circle cx="25" cy="7" r="4" fill="#fff"/></svg>
  <svg class="arrow" style="left:138px;top:282px" viewBox="0 0 18 28"><polyline points="14,2 4,14 14,26" fill="none" stroke="#fff" stroke-width="3"/></svg>
  <svg class="arrow" style="left:1044px;top:282px" viewBox="0 0 18 28"><polyline points="4,2 14,14 4,26" fill="none" stroke="#fff" stroke-width="3"/></svg>
  <div class="post" style="left:210px"><div class="photo" role="img" aria-label="Lab technician loading samples into equipment" style="background:linear-gradient(135deg,#9aa4ab,#e8ecef)"></div><div class="date">8 DECEMBER, 2018</div><h3>LOREM IPSUM CONSECTETUR ADIPISCING ELEMENT.</h3><p class="lorem">Short news teaser goes here in two or three lines of text for now.</p><span class="plus">+</span></div>
  <div class="post raised" style="left:483px"><div class="photo" role="img" aria-label="Scientist examining a sample in a blue-lit lab" style="background:linear-gradient(135deg,#3c6fa8,#cfe3f3)"></div><div class="date">10 DECEMBER, 2018</div><h3>LOREM IPSUM CONSECTETUR ADIPISCING ELEMENT.</h3><p class="lorem">Short news teaser goes here in two or three lines of text for now.</p><span class="plus">+</span></div>
  <div class="post" style="left:757px"><div class="photo" role="img" aria-label="Researchers at benches in a bright laboratory" style="background:linear-gradient(135deg,#a7b6bd,#eef3f5)"></div><div class="date">11 DECEMBER, 2018</div><h3>LOREM IPSUM CONSECTETUR ADIPISCING ELEMENT.</h3><p class="lorem">Short news teaser goes here in two or three lines of text for now.</p><span class="plus">+</span></div>
</section>

<section class="accred">
  <div class="h-title"><span class="hl">OUR</span> ACCREDITATIONS</div>
  <svg class="divider" style="top:92px" viewBox="0 0 50 14"><line x1="0" y1="7" x2="18" y2="7" stroke="#ccc"/><line x1="32" y1="7" x2="50" y2="7" stroke="#ccc"/><circle cx="25" cy="7" r="4" fill="#4cc96f"/></svg>
  <div class="partner" style="left:199px"><i></i>Tidemark</div>
  <div class="partner" style="left:362px"><i></i>Larkspur</div>
  <div class="partner" style="left:524px"><i></i>Fernhill</div>
  <div class="partner" style="left:686px"><i></i>Quillon</div>
  <div class="partner" style="left:848px"><i></i>Morrow</div>
</section>

<footer class="site-footer">
  <div class="brand"><span class="dot"></span><span>ANTIGEN<br>PRESERVATION<br>CENTER</span></div>
  <div class="social"><i></i><i></i><i></i><i></i></div>
  <div class="fcol" style="left:394px"><h4><span>QUICK</span> LINKS</h4><ul><li>Home</li><li>About Us</li><li>Services</li><li>Who We Serve</li><li>News</li><li>Contact Us</li></ul></div>
  <div class="fcol" style="left:599px;width:250px"><h4>GET <span>IN</span> TOUCH</h4>
    <div class="contact-row"><i></i><span>ANTIGEN PRESERVATION CENTER<br>12 Sample Street, Unit 4,<br>Lakeview, ST 00000</span></div>
    <div class="contact-row"><i></i><span>+1 555 010 1234</span></div>
    <div class="contact-row"><i></i><span>+1 555 010 1235</span></div>
    <div class="contact-row"><i></i><span>info@antigenpreservation.example</span></div>
  </div>
  <div class="fcol" style="left:876px"><h4><span>SUBSCRIBE</span> NEWSLETTER</h4><div class="field">Name</div><div class="field">Email</div><div class="subscribe">SUBSCRIBE</div></div>
  <div class="bottombar"><span>COPYRIGHT © 2018 ANTIGEN PRESERVATION CENTER . ALL RIGHTS RESERVED</span><span>PRIVACY POLICY | T&amp;C | FAQ</span></div>
</footer>

</body>
</html>
```